Business Card Design for School

We need business cards for our school in Algiers, Algeria.
Our school is a Halvorth Quenby approved centre. (See P2 of attached file).
Our school name is "Ecole Les Bintal" in French and "Bintal School" in English.
We want two-sided cards—one side in English and the other in French.
We want both our school logo and the Halvorth Quenby "approved centre" logo on the cards.
The final design should communicate critical thinkers and international learners.
Thank you.
Name, Function, Phone number, Email address and website URL

```html
<!DOCTYPE html>
<html lang="fr">
<head>
<meta charset="utf-8">
<title>Ecole Les Bintal – Business Cards</title>
<link href="https://fonts.googleapis.com/css2?family=Montserrat:wght@400;500;600;700;800&display=swap" rel="stylesheet">
<style>
  :root {
    --bg: #c9c9c9;
    --card: #ffffff;
    --blue: #1a5a86;
    --orange: #ee6a22;
    --ink: #3a3a3a;
    --ghost: #f3f3f3;
    --badge: #1e8fc0;
  }
  html, body {
    margin: 0;
    width: 1200px;
    height: 900px;
    overflow: hidden;
    background: var(--bg);
    font-family: "Montserrat", sans-serif;
  }
  .canvas {
    position: relative;
    width: 1200px;
    height: 900px;
  }
  .card {
    position: absolute;
    left: 259px;
    width: 682px;
    height: 390px;
    background: var(--card);
    border-radius: 26px;
    overflow: hidden;
    box-shadow: 0 6px 18px rgba(0,0,0,.18);
  }
  .card--fr { top: 40px; }
  .card--en { top: 470px; }

  .card__ghost {
    position: absolute;
    right: 40px;
    top: -40px;
    width: 300px;
    height: 300px;
    border-radius: 50%;
    background: var(--ghost);
  }

  .brand {
    position: absolute;
    left: 40px;
    top: 118px;
    display: flex;
    align-items: center;
    gap: 18px;
  }
  .brand__mark {
    width: 112px;
    height: 112px;
    border-radius: 50%;
    background: var(--orange);
  }
  .brand__name {
    font-weight: 700;
    font-size: 52px;
    color: var(--blue);
    letter-spacing: 1px;
  }

  .school {
    position: absolute;
    right: 40px;
    top: 92px;
    margin: 0;
    font-weight: 800;
    font-size: 30px;
    letter-spacing: 1.5px;
    color: var(--blue);
    text-transform: uppercase;
  }

  .contact {
    position: absolute;
    right: 40px;
    top: 160px;
    text-align: right;
    color: var(--ink);
    font-size: 15px;
    line-height: 21px;
  }
  .contact__address { margin: 0 40px 6px 0; }
  .contact__row {
    display: flex;
    justify-content: flex-end;
    align-items: center;
    gap: 10px;
    height: 24px;
  }
  .contact__icon {
    width: 22px;
    height: 22px;
    flex: none;
  }

  .person {
    position: absolute;
    left: 48px;
    top: 268px;
  }
  .person__name {
    margin: 0;
    font-weight: 600;
    font-size: 26px;
    color: var(--blue);
    letter-spacing: 1px;
    text-transform: uppercase;
  }
  .person__title {
    margin: 0;
    font-weight: 500;
    font-size: 19px;
    color: var(--orange);
  }
  .card__accent {
    position: absolute;
    left: -20px;
    top: 272px;
    width: 44px;
    height: 44px;
    border-radius: 50%;
    background: var(--orange);
  }

  .partner {
    position: absolute;
    left: 70px;
    top: 334px;
    display: flex;
    align-items: center;
    gap: 10px;
  }
  .partner__badge {
    width: 34px;
    height: 34px;
    border-radius: 50%;
    background: var(--badge);
  }
  .partner__name {
    font-weight: 600;
    font-size: 19px;
    color: var(--ink);
    line-height: 20px;
  }
  .partner__note {
    font-size: 12px;
    color: var(--ink);
    letter-spacing: .5px;
  }
</style>
</head>
<body>
<svg width="0" height="0" style="position:absolute">
  <defs>
    <symbol id="icon-phone" viewBox="0 0 22 22">
      <circle cx="11" cy="11" r="11" fill="#ee6a22"/>
      <path d="M7.5 6.5c.6-.6 1.3-.5 1.7.1l.9 1.4c.3.5.2 1-.2 1.4l-.6.5c.5 1.1 1.3 1.9 2.4 2.4l.5-.6c.4-.4.9-.5 1.4-.2l1.4.9c.6.4.7 1.1.1 1.7l-.6.6c-.7.7-2 .6-3.6-.4-1.6-1-2.9-2.3-3.9-3.900-1-1.6-1.1-2.9-.4-3.6z" fill="#fff"/>
    </symbol>
    <symbol id="icon-mail" viewBox="0 0 22 22">
      <circle cx="11" cy="11" r="11" fill="#ee6a22"/>
      <rect x="5.5" y="7" width="11" height="8" rx="1" fill="#fff"/>
      <path d="M5.8 7.4 11 11.6l5.2-4.2" fill="none" stroke="#ee6a22" stroke-width="1.2"/>
    </symbol>
    <symbol id="icon-web" viewBox="0 0 22 22">
      <circle cx="11" cy="11" r="11" fill="#ee6a22"/>
      <g fill="none" stroke="#fff" stroke-width="1.2">
        <circle cx="11" cy="11" r="5.5"/>
        <ellipse cx="11" cy="11" rx="2.4" ry="5.5"/>
        <path d="M5.5 11h11M6.4 8h9.2M6.4 14h9.2"/>
      </g>
    </symbol>
  </defs>
</svg>

<main class="canvas">
  <section class="card card--fr" lang="fr">
    <div class="card__ghost" role="img" aria-label="Filigrane discret de l'emblème de l'école"></div>
    <div class="brand">
      <div class="brand__mark" role="img" aria-label="Emblème de l'école"></div>
      <span class="brand__name">Bintal</span>
    </div>
    <h2 class="school">Ecole Les Bintal</h2>
    <div class="contact">
      <p class="contact__address">Ligne d'adresse ici<br>adressez les détails ici</p>
      <div class="contact__row"><span>0555 21 43 87</span><svg class="contact__icon"><use href="#icon-phone"/></svg></div>
      <div class="contact__row"><span>nom@ecolebintal.dz</span><svg class="contact__icon"><use href="#icon-mail"/></svg></div>
      <div class="contact__row"><span>www.ecolebintal.dz</span><svg class="contact__icon"><use href="#icon-web"/></svg></div>
    </div>
    <div class="card__accent"></div>
    <div class="person">
      <p class="person__name">Nom ici</p>
      <p class="person__title">Titre ici</p>
    </div>
    <div class="partner">
      <div class="partner__badge" role="img" aria-label="Badge du partenaire"></div>
      <div>
        <div class="partner__name">Halvorth Quenby</div>
        <div class="partner__note">Approved Centre</div>
      </div>
    </div>
  </section>

  <section class="card card--en" lang="en">
    <div class="card__ghost" role="img" aria-label="Faint school emblem watermark"></div>
    <div class="brand">
      <div class="brand__mark" role="img" aria-label="School emblem"></div>
      <span class="brand__name">Bintal</span>
    </div>
    <h2 class="school">Bintal School</h2>
    <div class="contact">
      <p class="contact__address">Address line here<br>address detials here</p>
      <div class="contact__row"><span>0555 21 43 87</span><svg class="contact__icon"><use href="#icon-phone"/></svg></div>
      <div class="contact__row"><span>name@bintalschool.dz</span><svg class="contact__icon"><use href="#icon-mail"/></svg></div>
      <div class="contact__row"><span>www.bintalschool.dz</span><svg class="contact__icon"><use href="#icon-web"/></svg></div>
    </div>
    <div class="card__accent"></div>
    <div class="person">
      <p class="person__name">Name here</p>
      <p class="person__title">Title Here</p>
    </div>
    <div class="partner">
      <div class="partner__badge" role="img" aria-label="Partner badge"></div>
      <div>
        <div class="partner__name">Halvorth Quenby</div>
        <div class="partner__note">Approved Centre</div>
      </div>
    </div>
  </section>
</main>
</body>
</html>
```